New business card/stationary for a consulting company

I am looking for a clean and very professional looking business card for my consulting company as well as corresponding stationary. I am uploading our logo. I like simple and powerful for the feel. No graphics but I am open on everything else. Below is my contact information but would like the final to be in a version I can add my employees information into and print. Thank you.

Daniel Whitcombe
dan@fernlowadvisory.com
2837 North 9th Avenue, Summit Floor, Ashbury Heights, Ohio 60483
www.fernlowadvisory.com

Industry/Entity Type

Consulting

Contact Information for Business Card

Daniel Whitcombe
dan@fernlowadvisory.com
www.fernlowadvisory.com

Font styles to use
Serif
Sans Serif

Requirements
Must have
• Our logo and the business card details.
Nice to have
• our website www.fernlowadvisory.com

```html
<!DOCTYPE html>
<html lang="en">
<head>
<meta charset="utf-8">
<title>Fernlow Advisory — Business Card</title>
<link rel="stylesheet" href="https://fonts.googleapis.com/css2?family=Cinzel:wght@700&family=Mulish:wght@400&display=swap">
<style>
  :root {
    --navy: #262262;
    --paper: #ffffff;
    --contact: #d6d6e4;
  }
  html, body {
    margin: 0;
    padding: 0;
    width: 1200px;
    height: 681px;
    overflow: hidden;
    background: var(--paper);
  }
  .card {
    position: relative;
    width: 1200px;
    height: 681px;
    background: var(--paper);
    overflow: hidden;
  }
  .brand-name {
    position: absolute;
    top: 197px;
    left: 0;
    width: 100%;
    margin: 0;
    text-align: center;
    font-family: "Mulish", sans-serif;
    font-weight: 400;
    font-size: 62px;
    line-height: 1;
    letter-spacing: 9px;
    text-indent: 9px;
    color: var(--navy);
  }
  .rule {
    position: absolute;
    left: 0;
    top: 286px;
    width: 100%;
    height: 10px;
    background: var(--navy);
  }
  .details-band {
    position: absolute;
    left: 0;
    top: 312px;
    width: 100%;
    height: 369px;
    background: var(--navy);
  }
  .person-name {
    position: absolute;
    right: 47px;
    top: 350px;
    margin: 0;
    font-family: "Cinzel", serif;
    font-weight: 700;
    font-size: 60px;
    line-height: 1;
    letter-spacing: 7px;
    color: var(--paper);
    white-space: nowrap;
  }
  .contact-list {
    position: absolute;
    right: 54px;
    top: 418px;
    margin: 0;
    padding: 0;
    list-style: none;
    text-align: right;
    font-family: "Mulish", sans-serif;
    font-weight: 400;
    font-size: 40px;
    line-height: 54px;
    color: var(--contact);
    white-space: nowrap;
  }
</style>
</head>
<body>
  <main class="card">
    <h1 class="brand-name">FERNLOW ADVISORY</h1>
    <div class="rule"></div>
    <section class="details-band"></section>
    <h2 class="person-name">Daniel Whitcombe</h2>
    <ul class="contact-list">
      <li class="contact-email">dan@fernlowadvisory.com</li>
      <li class="contact-street">2837 North 9th Avenue, Summit Floor,</li>
      <li class="contact-city">Ashbury Heights, Ohio 60483</li>
      <li class="contact-web">www.fernlowadvisory.com</li>
    </ul>
  </main>
</body>
</html>
```